Simple Lawyer Business Card Design Project with gold foil

Looking for a double sided business card. I would like to incorporate two of the images I attached onto the card- a monogram M in a circle and the legal image.
I also added image # 2 as a possibility of how to incorporate both images and for the layout of the information.

Back Side: This side of card will be one version in maroon and one version in white. The logo/vector on back side of card with business name Crandell Legal Group. Shield/Vector should be placed above the Crandell Legal Group lettering in a gold foil press. Please use colors of attachment #3.

Front Side: front of card will be white. front of card could have the monogram M in circle on background (where the lightened scales are on the sample card), with company information over it- Crandell Legal Group. *please delete the crown image above the M* Would like to see the monogram logo in gold -Crandell Legal Group will be in gold foil. Everything on left side should be black font.

Velda Orsini, Esq.
Principal Attorney
Address: 18 Harwick Ave. Suite 212 Woodcliff Lake,
NJ 07419
Phone: 201-739-5186
Fax: 201-826-3947
Email: vorsini@kestrolaw.example
www.kestrolaw.example

Industry/Entity Type

Lawyer

Contact Information for Business Card

Velda Orsini, Esq.
Principal Attorney
Address: 18 Harwick Ave. Suite 212 Woodcliff Lake, NJ 07419
Phone: 201-739-5186
Fax: 201-826-3947
www.kestrolaw.example

Font styles to use
Serif
Other font styles liked:
• fonts on samples

Colors
ffffff

Requirements
Must have
• - The final files must conform w/:
• - https://www.quillpress.example/silk-w-stamped-foil-business-cards
• - https://www.quillpress.example/template-files/business-cards/3.5x2.zip
• - https://www.vidstream.example/watch?v=Q2rTk7LpZxa#action=share
• - we would ask that you upload single page .pdf files only.
• - we recommend a Rich Black value of C=60, M=40, Y=40, K=100
• - Foil mask files are set up just like our Spot UV mask files. The file will only be black and white. The black areas will show where you want the foil placed. White will show areas where you do not want the foil. When ordering a Foil Stamp job with Spot UV, you must provide separate mask files for the Foil (foil mask) and Spot UV (spuv mask). Up to Six files would need to be provided.
• - When using Foil, please keep in mind that Foil and UV can not overlap and we recommend avoiding the use of small/fine text or fonts for foil objects. For best results, please be sure foil coverage is less than 50% of the artwork area.
• - It’s also important to note that there may be up to 1/16" shift on the placement of the foil. Keep this in mind if you are trying to align foil with other printed artwork.
Should not have
• don't want anything cluttered

```html
<!DOCTYPE html>
<html lang="en">
<head>
<meta charset="utf-8">
<title>Crandell Legal Group – Business Card</title>
<link rel="stylesheet" href="https://fonts.googleapis.com/css2?family=PT+Sans:wght@400;700&display=swap">
<style>
  :root {
    --stage: #e9e6e3;
    --paper: #ffffff;
    --ink: #1b1b1b;
    --gold: #b8862f;
    --gold-light: #d4a451;
    --ring: #dadada;
    --rich-black: #050505;
  }
  * { box-sizing: border-box; margin: 0; padding: 0; }
  html, body {
    width: 1200px; height: 900px; overflow: hidden;
    background: var(--stage);
    font-family: "PT Sans", Arial, sans-serif;
  }
  .stage { position: relative; width: 1200px; height: 900px; }

  .card {
    position: absolute; overflow: hidden;
    box-shadow: 0 6px 18px rgba(0,0,0,.18);
  }

  /* Front */
  .card--front {
    left: 238px; top: 62px; width: 555px; height: 342px;
    background: var(--paper); color: var(--ink);
  }
  .monogram-ring {
    position: absolute; left: 272px; top: 21px;
    width: 300px; height: 300px; border-radius: 50%;
    border: 7px solid var(--ring);
  }
  .firm-name {
    color: var(--gold); font-weight: 400; white-space: nowrap;
    line-height: 1.1;
  }
  .card--front .firm-name {
    position: absolute; left: 270px; top: 138px; width: 280px;
    text-align: center; font-size: 28px;
  }
  .contact { position: absolute; left: 33px; top: 58px; width: 250px; }
  .contact__name { color: var(--gold); font-weight: 700; font-size: 18px; line-height: 1.2; }
  .contact__title { font-size: 15px; line-height: 1.3; }
  .contact__address { margin-top: 34px; font-size: 15px; line-height: 1.4; width: 245px; }
  .contact__list { list-style: none; margin-top: 30px; font-size: 15px; }
  .contact__list li { display: flex; align-items: center; height: 20px; }
  .contact__list svg { width: 11px; height: 11px; margin-right: 9px; fill: var(--gold); flex: none; }

  /* Back */
  .card--back {
    left: 459px; top: 518px; width: 560px; height: 344px;
    background: var(--rich-black);
    display: flex; flex-direction: column; align-items: center; justify-content: center;
    padding-top: 10px;
  }
  .brand-mark {
    width: 118px; height: 118px; border-radius: 50%;
    background: linear-gradient(135deg, #e2bb68, #a8792a);
    margin-bottom: 22px;
  }
  .card--back .firm-name { color: var(--gold-light); font-size: 30px; }
</style>
</head>
<body>
<main class="stage">

  <section class="card card--front" aria-label="Card front">
    <div class="monogram-ring" aria-hidden="true"></div>
    <p class="firm-name">Crandell Legal Group</p>

    <div class="contact">
      <p class="contact__name">Velda Orsini, Esq.</p>
      <p class="contact__title">Principal Attorney</p>
      <p class="contact__address">18 Harwick Ave. Suite 212 Woodcliff Lake, NJ 07419</p>
      <ul class="contact__list">
        <li>
          <svg viewBox="0 0 12 12" aria-label="Phone"><path d="M2.5 0.5 L4.5 0.5 L5 3.5 L3.6 4.4 C4.3 6 5.9 7.6 7.6 8.4 L8.5 7 L11.5 7.5 L11.5 9.5 C11.5 10.6 10.6 11.5 9.5 11.5 C4.5 11.2 0.8 7.5 0.5 2.5 C0.5 1.4 1.4 0.5 2.5 0.5 Z"/></svg>
          201-739-5186
        </li>
        <li>
          <svg viewBox="0 0 12 12" aria-label="Fax"><rect x="3" y="0.5" width="6" height="3.5"/><rect x="0.5" y="4.5" width="11" height="5" rx="1"/><rect x="3" y="8" width="6" height="3.5"/></svg>
          201-826-3947
        </li>
        <li>
          <svg viewBox="0 0 12 12" aria-label="Email"><path d="M0.5 2 H11.5 V10 H0.5 Z M1.5 3 L6 6.6 L10.5 3" fill="none" stroke="#b8862f" stroke-width="1.4"/></svg>
          vorsini@kestrolaw.example
        </li>
        <li>
          <svg viewBox="0 0 12 12" aria-label="Website"><circle cx="6" cy="6" r="5.2" fill="none" stroke="#b8862f" stroke-width="1.2"/><ellipse cx="6" cy="6" rx="2.2" ry="5.2" fill="none" stroke="#b8862f" stroke-width="1"/><line x1="0.8" y1="6" x2="11.2" y2="6" stroke="#b8862f" stroke-width="1"/></svg>
          www.kestrolaw.example
        </li>
      </ul>
    </div>
  </section>

  <section class="card card--back" aria-label="Card back">
    <div class="brand-mark" role="img" aria-label="Firm emblem in gold foil"></div>
    <p class="firm-name">Crandell Legal Group</p>
  </section>

</main>
</body>
</html>
```